Starlane Fireworks needs a web design and logo

We need a web design and logo for a fireworks business in Sydney Australia, we do public display, weddings, tv, theatrical, clubs and any other organisation that wants to do something special.
Name is Brightwell Fireworks & Pyrotechnics

```html
<!DOCTYPE html>
<html lang="en">
<head>
<meta charset="utf-8">
<title>Brightwell Fireworks &amp; Pyrotechnics</title>
<link href="https://fonts.googleapis.com/css2?family=Roboto:wght@300;400;500&display=swap" rel="stylesheet">
<style>
:root{
  --ink:#000;
  --paper:#fff;
  --muted:#6b6b6b;
  --soft:#bdbdbd;
  --night:#0b0a12;
}
*{margin:0;padding:0;box-sizing:border-box}
html,body{width:1200px;height:1000px;overflow:hidden;background:var(--paper)}
body{font-family:"Roboto",Arial,sans-serif;color:var(--ink);position:relative}
.site{position:absolute;left:522px;top:0;width:156px;height:1000px}
.abs{position:absolute;left:0;width:156px;text-align:center}
.hero{position:absolute;left:0;top:0;width:156px;height:100px;background:var(--ink);color:var(--paper)}
.hero-sky{position:absolute;left:0;top:0;width:156px;height:100px;
  background:radial-gradient(ellipse 40px 30px at 60px 55px,#6a3a5a 0%,#2a1a35 45%,rgba(0,0,0,0) 100%),
             radial-gradient(ellipse 30px 25px at 105px 45px,#4a3a60 0%,rgba(0,0,0,0) 100%),var(--night)}
.menu{position:absolute;left:3px;top:17px;width:10px;height:8px}
.brand{position:absolute;left:17px;top:17px;font-size:7.5px;font-weight:300;white-space:nowrap}
.hero-title{top:42px;font-size:13.5px;font-weight:300}
.hero-sub{top:62px;font-size:7.5px;font-weight:300;line-height:11px;padding:0 30px}
.dots{position:absolute;top:92px;left:62px;display:flex;gap:11px}
.dots span{width:4px;height:4px;border-radius:50%;background:var(--paper)}
.section-title{font-size:14px;font-weight:300;line-height:16px}
.photo{position:absolute}
.caption{font-size:5.5px;line-height:8px;padding:0 40px}
.about{font-size:7.3px;line-height:8.6px;color:var(--muted);padding:0 22px;font-weight:300}
.pricing{position:absolute;left:0;top:447px;width:156px;height:251px;background:var(--ink);color:var(--paper)}
.price{font-size:7.5px;line-height:9px}
.plan{font-size:9.5px;font-weight:300;color:#e6e6e6}
.detail{font-size:7.3px;color:var(--soft);font-weight:300}
.contact-label{font-size:8px;line-height:9px;font-weight:300}
.signup-note{font-size:6px}
.signup{position:absolute;left:33px;top:929px;width:95px;height:13px;display:flex}
.signup-field{flex:1;border:1px solid var(--ink);font-size:4.5px;color:var(--muted);padding:3px 2px;line-height:6px;text-align:left}
.signup-go{width:13px;background:var(--ink);color:var(--paper);font-size:5px;font-weight:500;line-height:13px;text-align:center}
.footer{position:absolute;left:0;top:962px;width:156px;height:38px;background:var(--ink);display:flex;justify-content:center;align-items:center;gap:12px}
.footer span{width:11px;height:11px;border-radius:50%;background:var(--paper)}
</style>
</head>
<body>
<div class="site">
  <header class="hero">
    <div class="hero-sky" role="img" aria-label="Night sky filled with colourful fireworks bursts"></div>
    <svg class="menu" viewBox="0 0 10 8"><rect y="0" width="10" height="1.6" fill="#fff"/><rect y="3.2" width="10" height="1.6" fill="#fff"/><rect y="6.4" width="10" height="1.6" fill="#fff"/></svg>
    <div class="brand">Brightwell Fireworks &amp; Pyrotechnics</div>
    <h1 class="abs hero-title" style="font-weight:300">Public Display Events</h1>
    <p class="abs hero-sub">Make Something Special. For Everyone to See</p>
    <div class="dots"><span></span><span></span><span></span></div>
  </header>

  <h2 class="abs section-title" style="top:99px">what we do</h2>
  <div class="photo" style="left:29px;top:115px;width:98px;height:74px;background:linear-gradient(135deg,#2c3e3a,#8a7a45 55%,#3a2a20)" role="img" aria-label="Technician preparing pyrotechnic shells"></div>
  <p class="abs caption" style="top:190px">Click here to see how Pyrotechnics work!</p>
  <div class="photo" style="left:28px;top:208px;width:100px;height:59px;background:linear-gradient(180deg,#1a1a22,#6a6f78 50%,#2a2420)" role="img" aria-label="Stage show with pyrotechnic fountains"></div>
  <p class="abs caption" style="top:268px">Make your show unforgettable with timed pyrotechnics?</p>
  <div class="photo" style="left:30px;top:288px;width:96px;height:72px;background:radial-gradient(circle at 45% 45%,#b89a70 0%,#4a3a2a 35%,#050505 75%)" role="img" aria-label="Golden firework burst at night"></div>
  <p class="abs caption" style="top:361px">Endless variations and durration available?</p>
  <p class="abs about" style="top:378px">We need a web design and logo for a fireworks business in Sydney Australia, we do public display, weddings, tv, theatrical, clubs and any other organisation that wants to do something special.<br>More Info About Company, More Pictures</p>

  <section class="pricing">
    <h2 class="abs section-title" style="top:0">pricing</h2>
    <p class="abs price" style="top:29px">$xxx.xx<br>per hour</p>
    <p class="abs plan" style="top:57px">Pricing Quote 3</p>
    <p class="abs detail" style="top:75px">with details</p>
    <p class="abs price" style="top:110px">$xxx.xx<br>per hour</p>
    <p class="abs plan" style="top:138px">Pricing Quote 3</p>
    <p class="abs detail" style="top:156px">with details</p>
    <p class="abs price" style="top:191px">$xxx.xx<br>per hour</p>
    <p class="abs plan" style="top:219px">Pricing Quote 3</p>
    <p class="abs detail" style="top:237px">with details</p>
  </section>

  <h2 class="abs section-title" style="top:703px">get in touch</h2>
  <svg style="position:absolute;left:48px;top:722px" width="60" height="58" viewBox="0 0 60 58">
    <path d="M4 6 C8 1 14 0 16 3 L24 16 C26 19 24 22 20 24 C18 25 18 27 20 31 C25 40 31 46 40 51 C44 53 46 52 47 50 C49 46 52 44 55 46 L58 49 C61 52 59 56 54 57 C40 59 22 48 10 30 C3 20 1 11 4 6 Z" fill="#000"/>
  </svg>
  <p class="abs contact-label" style="top:784px">phone<br>(000) 000-0000</p>
  <svg style="position:absolute;left:49px;top:820px" width="58" height="58" viewBox="0 0 58 58">
    <circle cx="29" cy="29" r="26.5" fill="none" stroke="#000" stroke-width="4"/>
    <text x="29" y="41" text-anchor="middle" font-family="Roboto, Arial, sans-serif" font-size="36" font-weight="500">@</text>
  </svg>
  <p class="abs contact-label" style="top:882px">email<br>hello@brightwellpyro.com</p>
  <p class="abs signup-note" style="top:916px">or we'll reach out to you</p>
  <div class="signup"><div class="signup-field">Enter Email Address</div><div class="signup-go">GO</div></div>

  <footer class="footer" aria-label="Social links"><span></span><span></span><span></span><span></span></footer>
</div>
</body>
</html>
```